IT Services company requires a services website design with integrated blog

We at Brambleway Code Haulage primarily provide application migration consultancy (e.g. moving applications from Paneview QR to Paneview 5) and application virtualization (e.g. Dunmore Box-K) consultancy.This process is commonly known as 'packaging' but doesnt involve cardboard boxes ;) (however, I am happy to use that visual analogy if you want to use any box graphics) We also provide application compatibility testing, software auditing and application portfolio management.

We are looking for a complete redesign of our current horrible diy attempt at a website at www.brambleway-example.com. We have had created a rebranded logo (attached files and fonts) and a rebranded business card (also attached) We would like the website to match the same/similar colors and styling as these.

I want to redisgn the website so that the main focus of this website is to show our subject matter expertise with a blog and should take up most of the websites real estate and focus on the home screen. Then if the customer wants, they can use our services to help them in their own application migration/deployment projects by browsing our details in links/buttons somewhere

In any of the designs, please do not include my Velharo or Dunmore partnerships.  Thank you

Target Market(s)

Application packagers / engineers looking for technical articles

Application migration project managers

Industry/Entity Type

Real Estate

Requirements
Must have
• This site is primarily a blog site. The blog should have buttons to share each article on social media site. It should be easy for me to create or edit new blog articles (have technical skills but not creative ones). Each article should also allow for comments (do not require approval but should allow for admin removal) but do not add like/vote buttons because i do not expect large enough traffic and could be determental.

There should be a contact page to host contact information and an email box that goes to enquiries@brambleway-example.com

The other pages should include About us and Services (placeholder text to be used as current site text needs overhauling but original text can be used in the design just remember when placing that the text may shorten or increase etc.)

All text has to be easily editable (no over use of text in images where possible)
Nice to have
• An email notification of new comments to articles sent to webadmin@brambleway-example.com

Newsletter subscription
Should not have
• Do not include vote/like buttons or website counters. Initial traffic is not going to be large enough to warrant these features and may reflect badly on the site.

No logon features. Site content and commenting should be open access

No opinion polls

No why choose us section from current website

Do not include partner information in new site (Velharo and Dunmore)

DO NOT JUST REPLICATE EXISTING WEBSITE FEATURES, PLEASE REFER TO THIS BRIEF. THIS SITE NEEDS TO PRIMARILY BE A BLOG

```html
<!DOCTYPE html>
<html lang="en">
<head>
<meta charset="utf-8">
<title>Brambleway Code Haulage</title>
<link href="https://fonts.googleapis.com/css2?family=Oswald:wght@400;600&family=Open+Sans:wght@400;600;700&display=swap" rel="stylesheet">
<style>
:root{
  --dark:#23262a;
  --dark-2:#34383d;
  --hero-top:#1d2a33;
  --hero-glow:#3f6f86;
  --orange:#f39a1e;
  --blue:#2aa3d8;
  --green:#5fae2e;
  --text:#555a5f;
  --muted:#8a8f94;
  --light:#eeeeee;
  --line:#d9d9d9;
  --white:#ffffff;
  --wood-a:#8a5a32;
  --wood-b:#5c3a1f;
}
*{box-sizing:border-box;margin:0;padding:0}
html,body{width:1200px;height:2460px;overflow:hidden}
body{position:relative;background:var(--white);font-family:"Open Sans",Arial,sans-serif;color:var(--text)}
.abs{position:absolute}

/* header */
.site-header{left:0;top:0;width:1200px;height:200px;background:linear-gradient(#2b2e33,var(--dark))}
.brand{left:0;top:56px;width:1200px;display:flex;justify-content:center;align-items:center;gap:14px}
.brand-mark{width:46px;height:46px;background:var(--blue)}
.brand-name{font-weight:600;font-size:30px;color:var(--white)}
.main-nav{left:220px;top:160px;width:760px;height:40px;display:flex;align-items:center;font-size:14px;color:var(--white)}
.main-nav a{color:var(--white);text-decoration:none;padding:0 22px;height:40px;line-height:40px}
.main-nav a.active{background:var(--orange)}
.nav-phone{margin-left:auto;display:flex;align-items:center;gap:8px;font-weight:600}

/* hero */
.hero{left:0;top:200px;width:1200px;height:380px;background:radial-gradient(ellipse at 60% 50%,var(--hero-glow),var(--hero-top) 70%)}
.hero-title{left:248px;top:30px;font-family:"Oswald",Arial,sans-serif;font-weight:600;font-size:36px;line-height:42px;color:var(--white)}
.hero-devices{left:300px;top:124px;width:680px;height:166px;background:linear-gradient(135deg,#1b1f24,#3a86b4 55%,#2c3136);border-radius:6px}
.hero-shelf{left:220px;top:290px;width:780px;height:90px;background:linear-gradient(var(--wood-a),var(--wood-b))}
.hero-label{left:248px;top:306px;font-family:"Oswald",Arial,sans-serif;font-weight:600;font-size:34px;color:var(--white);letter-spacing:1px}

/* services */
.services{left:192px;top:620px;width:816px;display:flex;justify-content:space-between}
.service{width:240px;text-align:center}
.service svg{display:block;margin:0 auto 14px}
.service h3{font-family:"Oswald",Arial,sans-serif;font-weight:400;font-size:16px;margin-bottom:8px}
.service p{font-size:12px;line-height:18px;color:var(--muted)}
.service.orange h3{color:var(--orange)}
.service.blue h3{color:var(--blue)}
.service.green h3{color:var(--green)}
.search{left:248px;top:894px;width:700px;height:36px;display:flex;gap:20px}
.search-field{flex:1;border:1px solid var(--line);border-radius:3px;display:flex;align-items:center;gap:8px;padding:0 12px;font-size:13px;color:var(--muted)}
.search-button{width:220px;background:var(--green);color:var(--white);font-size:14px;font-weight:600;display:flex;align-items:center;justify-content:center;border-radius:3px}

/* featured articles band */
.featured{left:0;top:952px;width:1200px;height:428px;background:linear-gradient(var(--dark-2),var(--dark))}
.featured-phone{left:210px;top:14px;width:300px;height:414px;background:linear-gradient(#111316,#3a4048 60%,#1a1d21);border-radius:30px 30px 0 0}
.featured-title{left:560px;top:26px;font-family:"Oswald",Arial,sans-serif;font-weight:600;font-size:30px;color:var(--white)}
.featured-intro{left:560px;top:70px;font-size:14px;font-weight:600;color:var(--white)}
.article-list{left:560px;top:100px;list-style:none;font-size:13px;color:#c9cdd1}
.article-list li{height:30px;display:flex;align-items:center;gap:10px}
.featured-devices{left:780px;top:316px}

/* blog */
.blog-heading{left:192px;top:1408px;font-family:"Oswald",Arial,sans-serif;font-weight:600;font-size:30px;color:var(--blue)}
.blog-sub{left:192px;top:1452px;font-size:13px;color:var(--text)}
.blog-sub b{color:var(--orange)}
.blog-rule{left:192px;top:1480px;width:816px;height:1px;background:var(--line)}
.post{background:var(--light);padding:20px}
.post h2{font-family:"Oswald",Arial,sans-serif;font-weight:400;font-size:20px;color:var(--dark);margin-bottom:10px}
.post p{font-size:12px;line-height:18px;color:var(--text)}
.post-meta{display:flex;gap:6px;margin-top:16px;align-items:center}
.share{font-size:10px;color:var(--white);background:var(--muted);padding:2px 8px;border-radius:2px}
.comments{font-size:10px;color:var(--muted);margin-left:6px}
.post-one{left:192px;top:1500px;width:312px;height:200px}
.photo-one{left:508px;top:1500px;width:500px;height:240px;background:linear-gradient(135deg,#7b8a99,#2f4a6b 60%,#a8b2bc)}
.photo-two{left:192px;top:1760px;width:490px;height:200px;background:linear-gradient(135deg,#c9cdd0,#7f8b95 50%,#e4e6e8)}
.post-two{left:688px;top:1780px;width:320px;height:180px}

/* contact */
.contact{left:0;top:2032px;width:1200px;height:360px;background:#e6e6e6}
.contact h2{left:192px;top:28px;font-family:"Oswald",Arial,sans-serif;font-weight:600;font-size:28px;color:var(--dark)}
.contact-list{left:192px;top:86px;list-style:none;font-size:12px;line-height:18px;color:var(--text)}
.contact-list li{display:flex;gap:10px;margin-bottom:12px}
.contact-list a{color:var(--blue);text-decoration:none}
.contact-button{left:192px;top:272px;width:150px;height:36px;background:var(--green);color:var(--white);font-size:14px;font-weight:600;display:flex;align-items:center;justify-content:center;border-radius:3px}
.contact-map{left:480px;top:70px;width:520px;height:260px;background:linear-gradient(135deg,#f1efe6,#d9dccf);border:1px solid var(--line)}

/* footer */
.site-footer{left:192px;top:2392px;width:816px;height:68px;display:flex;align-items:center;font-size:11px;color:var(--muted)}
.site-footer nav{display:flex;gap:22px}
.site-footer .copyright{margin-left:auto}
</style>
</head>
<body>

<header class="site-header abs">
  <div class="brand abs">
    <span class="brand-mark"></span>
    <span class="brand-name">Brambleway Code Haulage</span>
  </div>
  <nav class="main-nav abs">
    <a href="#">Home</a>
    <a href="#">Blog</a>
    <a href="#">About Us</a>
    <a href="#">Our Services</a>
    <a href="#" class="active">Contact</a>
    <span class="nav-phone">
      <svg width="14" height="14" viewBox="0 0 24 24"><path fill="#fff" d="M6.6 10.8a15 15 0 0 0 6.6 6.6l2.2-2.2a1 1 0 0 1 1-.25 11.4 11.4 0 0 0 3.6.57 1 1 0 0 1 1 1V20a1 1 0 0 1-1 1A17 17 0 0 1 3 4a1 1 0 0 1 1-1h3.5a1 1 0 0 1 1 1c0 1.25.2 2.45.57 3.6a1 1 0 0 1-.25 1z"/></svg>
      0800 555 0142
    </span>
  </nav>
</header>

<section class="hero abs">
  <h1 class="hero-title abs">The detailed organisation and implementation<br>of a complex operation</h1>
  <div class="hero-devices abs" role="img" aria-label="Laptop, tablet and smartphone showing software screens"></div>
  <div class="hero-shelf abs" role="img" aria-label="Wooden shelf with a green arrow ribbon"></div>
  <div class="hero-label abs">LOGISTICS</div>
</section>

<section class="services abs">
  <div class="service orange">
    <svg width="64" height="56" viewBox="0 0 64 56"><rect x="8" y="6" width="48" height="34" rx="3" fill="none" stroke="#f39a1e" stroke-width="4"/><rect x="22" y="44" width="20" height="6" fill="#f39a1e"/></svg>
    <h3>INITIALISATION</h3>
    <p>Improve your packaging workflow by ensuring that the right information is collected, recording every step so packaging and updating go smoothly.</p>
  </div>
  <div class="service blue">
    <svg width="64" height="56" viewBox="0 0 64 56"><rect x="6" y="14" width="40" height="34" rx="3" fill="none" stroke="#2aa3d8" stroke-width="4"/><rect x="18" y="6" width="40" height="34" rx="3" fill="none" stroke="#2aa3d8" stroke-width="4"/></svg>
    <h3>PORTFOLIO MANAGEMENT</h3>
    <p>Improve your packaging workflow by ensuring that the right information is collected, recording every step so packaging and updating go smoothly.</p>
  </div>
  <div class="service green">
    <svg width="64" height="56" viewBox="0 0 64 56"><path d="M8 18 32 6l24 12v24L32 54 8 42z" fill="none" stroke="#5fae2e" stroke-width="4"/><path d="M8 18l24 12 24-12M32 30v24" fill="none" stroke="#5fae2e" stroke-width="4"/></svg>
    <h3>PACKAGING</h3>
    <p>Improve your packaging workflow by ensuring that the right information is collected, recording every step so packaging and updating go smoothly.</p>
  </div>
</section>

<div class="search abs">
  <div class="search-field">
    <svg width="14" height="14" viewBox="0 0 24 24"><circle cx="10" cy="10" r="7" fill="none" stroke="#8a8f94" stroke-width="3"/><path d="M15 15l7 7" stroke="#8a8f94" stroke-width="3"/></svg>
    Search articles
  </div>
  <div class="search-button">Search Blog</div>
</div>

<section class="featured abs">
  <div class="featured-phone abs" role="img" aria-label="Smartphone showing a blog article on screen"></div>
  <h2 class="featured-title abs">LATEST ARTICLES</h2>
  <p class="featured-intro abs">Technical notes for packagers and migration teams</p>
  <ul class="article-list abs">
    <li><svg width="12" height="12" viewBox="0 0 12 12"><path d="M2 1l6 5-6 5" fill="none" stroke="#5fae2e" stroke-width="2"/></svg>Moving apps from Paneview QR to Paneview 5</li>
    <li><svg width="12" height="12" viewBox="0 0 12 12"><path d="M2 1l6 5-6 5" fill="none" stroke="#5fae2e" stroke-width="2"/></svg>Planning an application virtualisation pilot</li>
    <li><svg width="12" height="12" viewBox="0 0 12 12"><path d="M2 1l6 5-6 5" fill="none" stroke="#5fae2e" stroke-width="2"/></svg>Five checks before you sequence a package</li>
    <li><svg width="12" height="12" viewBox="0 0 12 12"><path d="M2 1l6 5-6 5" fill="none" stroke="#5fae2e" stroke-width="2"/></svg>Auditing licences without the headache</li>
    <li><svg width="12" height="12" viewBox="0 0 12 12"><path d="M2 1l6 5-6 5" fill="none" stroke="#5fae2e" stroke-width="2"/></svg>Shims and fixes for legacy installers</li>
    <li><svg width="12" height="12" viewBox="0 0 12 12"><path d="M2 1l6 5-6 5" fill="none" stroke="#5fae2e" stroke-width="2"/></svg>Keeping your app portfolio lean</li>
  </ul>
  <svg class="featured-devices abs" width="200" height="80" viewBox="0 0 200 80">
    <rect x="2" y="10" width="40" height="64" rx="6" fill="none" stroke="#8a8f94" stroke-width="3"/>
    <rect x="70" y="2" width="120" height="76" rx="6" fill="none" stroke="#8a8f94" stroke-width="3"/>
    <circle cx="182" cy="40" r="3" fill="#8a8f94"/>
  </svg>
</section>

<h2 class="blog-heading abs">BLOG</h2>
<p class="blog-sub abs">See our recent <b>ARTICLES</b> here</p>
<div class="blog-rule abs"></div>

<article class="post post-one abs">
  <h2>PACKAGING CHECKLIST</h2>
  <p>A practical list of the steps we follow before, during and after building a package, so nothing is missed on release day.</p>
  <div class="post-meta"><span class="share">Share</span><span class="share">Post</span><span class="comments">2 Comments</span></div>
</article>
<div class="photo-one abs" role="img" aria-label="Photograph of engineers reviewing a project"></div>

<div class="photo-two abs" role="img" aria-label="Illustration of a tablet displaying a 3D city model"></div>
<article class="post post-two abs">
  <h2>COMPATIBILITY TESTING</h2>
  <p>How we test legacy applications on a new platform and record the fixes, so the move stays quick and predictable.</p>
  <div class="post-meta"><span class="share">Send</span><span class="share">Save</span><span class="comments">2 Comments</span></div>
</article>

<section class="contact abs">
  <h2 class="abs">CONTACT</h2>
  <ul class="contact-list abs">
    <li><svg width="14" height="16" viewBox="0 0 24 28"><path d="M12 0a9 9 0 0 0-9 9c0 7 9 19 9 19s9-12 9-19a9 9 0 0 0-9-9zm0 12a3 3 0 1 1 0-6 3 3 0 0 1 0 6z" fill="#8a8f94"/></svg><span>17 Ashcombe Row, Fenwick Green<br>Essex XX1 2AB United Kingdom</span></li>
    <li><svg width="14" height="14" viewBox="0 0 24 24"><rect x="1" y="4" width="22" height="16" fill="none" stroke="#8a8f94" stroke-width="2"/><path d="M1 4l11 9 11-9" fill="none" stroke="#8a8f94" stroke-width="2"/></svg><a href="#">enquiries@brambleway-example.com</a></li>
    <li><svg width="14" height="14" viewBox="0 0 24 24"><path fill="#8a8f94" d="M6.6 10.8a15 15 0 0 0 6.6 6.6l2.2-2.2a1 1 0 0 1 1-.25 11.4 11.4 0 0 0 3.6.57 1 1 0 0 1 1 1V20a1 1 0 0 1-1 1A17 17 0 0 1 3 4a1 1 0 0 1 1-1h3.5a1 1 0 0 1 1 1c0 1.25.2 2.45.57 3.6a1 1 0 0 1-.25 1z"/></svg><span>0800 555 0142<br>0800 555 0178</span></li>
  </ul>
  <div class="contact-button abs">Get in Touch</div>
  <div class="contact-map abs" role="img" aria-label="Street map showing the office location"></div>
</section>

<footer class="site-footer abs">
  <nav><span>Home</span><span>Blog</span><span>About Us</span><span>Our Services</span><span>Contact</span></nav>
  <span class="copyright">Copyright © 2013 Brambleway Code Haulage Ltd. All Rights Reserved.</span>
</footer>

</body>
</html>
```